BRIM needs a contemporary simple brochure

We help companies understand their customers, and we would like to send a minimalistic card/brochure to potential clients to introduce our company. The card will be A6 in size (ie A5 folded once) and so will have a front, an inside front, and inside back, and a back page. It can either be portrait or landscape.
It should convey contemporary/modern, bold, fun, uncomplicated/simplicity, be clean/uncluttered, and use friendly and easy to read fonts.
Attached is the information the brochure/card should contain, together with colour palatte and another document which shows our logo, existing stationary etc to give you a feel of the brand. The background of the card could be black, yellow or white (or a combination). thanks, dave
Updates
Hi everyone. Just to let you know that the card will be A6 size, will have a matt laminate finish and can include spot uv. thanks, dave
Reason: Hi, I am looking for some better quality designs so i have extended the deadline and significantly increased the budget. thanks, dave
Target Market(s)
Marketing professionals in large corporates
Industry/Entity Type
It Company
Requirements
Must have
- use our company colours (attached)

```html
<!DOCTYPE html>
<html lang="en">
<head>
<meta charset="utf-8">
<title>BRIM – Customer &amp; Shopper Market Research brochure</title>
<link href="https://fonts.googleapis.com/css2?family=Exo+2:wght@400;700&display=swap" rel="stylesheet">
<style>
  :root {
    --brand-yellow: #ffcc00;
    --ink: #3c3c3c;
    --paper: #ffffff;
    --backdrop: #1d1d1d;
    --fold: rgba(0, 0, 0, 0.28);
  }
  * { box-sizing: border-box; margin: 0; padding: 0; }
  html, body { width: 1200px; height: 848px; overflow: hidden; }
  body {
    background: var(--backdrop);
    font-family: "Exo 2", Arial, sans-serif;
    color: var(--ink);
    position: relative;
  }
  .spread {
    position: absolute;
    top: 241px;
    width: 520px;
    height: 365px;
    display: flex;
    box-shadow: 0 10px 30px rgba(0,0,0,0.5);
  }
  .spread--outside { left: 60px; background: var(--brand-yellow); }
  .spread--inside { left: 620px; background: var(--paper); }
  .panel { position: relative; width: 260px; height: 100%; }
  .panel + .panel { border-left: 1px solid var(--fold); }

  .brand-name {
    font-weight: 700;
    line-height: 1;
    letter-spacing: 0.5px;
    display: inline-block;
  }

  .gear-cluster {
    position: absolute;
    left: 14px; top: 12px;
    width: 118px; height: 150px;
    border-radius: 50% 50% 46% 12% / 30% 30% 60% 12%;
    background: radial-gradient(circle at 35% 30%, rgba(60,60,60,0.45), rgba(60,60,60,0.15) 70%, rgba(60,60,60,0));
  }
  .gear-cluster--large { left: 30px; top: 18px; width: 110px; height: 160px; }

  /* outside: back panel */
  .back__contact { position: absolute; left: 40px; bottom: 40px; }
  .back .brand-name { font-size: 30px; }
  .back__address { margin-top: 8px; font-size: 11px; line-height: 1.45; }

  /* outside: front panel */
  .front__brand { position: absolute; right: 22px; bottom: 38px; text-align: right; }
  .front .brand-name { font-size: 44px; }
  .front__tagline { margin-top: 6px; font-size: 12px; line-height: 1.3; }

  /* inside: services panel */
  .services__block { position: absolute; left: 74px; top: 252px; display: flex; gap: 8px; }
  .services .brand-name { font-size: 19px; color: var(--brand-yellow); }
  .services__list { list-style: none; font-size: 8.5px; line-height: 1.28; margin-top: 2px; }

  /* inside: about panel */
  .about__intro { position: absolute; left: 17px; top: 48px; width: 224px; font-size: 8.3px; line-height: 1.5; text-align: justify; letter-spacing: 0.2px; }
  .about__name-box {
    display: inline-block;
    background: var(--brand-yellow);
    padding: 3px 6px;
    margin-right: 3px;
    vertical-align: -2px;
  }
  .about__name-box .brand-name { font-size: 14px; }
  .about__headline { position: absolute; left: 17px; top: 303px; font-size: 11px; font-weight: 700; letter-spacing: 0.4px; }
  .about__cta {
    position: absolute; left: 17px; top: 321px; width: 224px; height: 21px;
    background: var(--brand-yellow); color: var(--paper);
    font-size: 10px; line-height: 21px; padding-left: 10px;
  }
</style>
</head>
<body>

<section class="spread spread--outside" aria-label="Brochure outside">
  <div class="panel back">
    <div class="back__contact">
      <div class="brand-name">BRIM</div>
      <p class="back__address">
        Level 3, 14 Harbour Lane,<br>
        Glebe, NSW, 2037<br>
        02 9555 0142<br>
        hello@brimmr.com.au
      </p>
    </div>
  </div>
  <div class="panel front">
    <div class="gear-cluster gear-cluster--large" role="img" aria-label="Cluster of interlocking gears"></div>
    <div class="front__brand">
      <div class="brand-name">BRIM</div>
      <p class="front__tagline">Customer &amp; Shopper<br>Market Research</p>
    </div>
  </div>
</section>

<section class="spread spread--inside" aria-label="Brochure inside">
  <div class="panel services">
    <div class="gear-cluster" role="img" aria-label="Cluster of interlocking gears"></div>
    <div class="services__block">
      <div class="brand-name">BRIM</div>
      <ul class="services__list">
        <li>New Product Development</li>
        <li>Product Testing</li>
        <li>Shopper Research</li>
        <li>Customer Segmentation</li>
        <li>Online Communities</li>
        <li>Customer Experience</li>
        <li>Visualisation</li>
        <li>Bespoke Research</li>
      </ul>
    </div>
  </div>
  <div class="panel about">
    <p class="about__intro">
      <span class="about__name-box"><span class="brand-name">BRIM</span></span>
      is a progressive, technology friendly market research agency, specialising in customer and shopper research. We help you connect with your customers so you can understand current behaviours, test new ideas, benchmark against your competition, plus a whole lot more. We do this by combining innovative methods, creative thinking, research expertise and a deep understanding of shopper and consumer decision-making.
    </p>
    <h2 class="about__headline">UNDERSTAND YOUR CUSTOMERS BETTER</h2>
    <p class="about__cta">Find out more at www.brimmr.com.au</p>
  </div>
</section>

</body>
</html>
```